Stationary Design to Complement our Website

We would like template designed for word documents that we can use for headed paper. The template should complement the style of our website & incorporate our existing logo. https://www.velmorantravel.com/

The header and footer design should be sperate PNG or JPEG files that we can copy and paste into word header and footers. They should work on A4 & letter sized papers.

Note the main web colours are as follows:

Black
HEX code #2b2c2b
C=71 M=64 Y=64 K=65
RGB 43,44,43

Green
HEX code #116c49
C=88 M=33 Y=82 K=24
RGB 17,108,73

Current fonts are ALEO & Gilroy.

Fonts and colours in new design don't have to match website exactly but should be complementary.

Font styles to use
Serif

Requirements
Must have
• a simple design that complements our website.
Some kind of graphic on the top & some sort of graphic on the bottom. Not just plain logo on top.
designs that incorporate the clouds might look good
Can also incorporate 5* rate harbor rating
Should not have
• no photographs included on the design

```html
<!DOCTYPE html>
<html lang="en">
<head>
<meta charset="UTF-8">
<title>Velmoran Travel Letterhead</title>
<link rel="stylesheet" href="https://fonts.googleapis.com/css2?family=Aleo:wght@400;700&family=Urbanist:wght@600;800&display=swap">
<style>
  :root {
    --ink: #2b2c2b;
    --green: #116c49;
    --grey: #555655;
    --paper: #fefefe;
  }
  * { margin: 0; padding: 0; box-sizing: border-box; }
  html, body { width: 849px; height: 1200px; overflow: hidden; background: var(--paper); }
  .sheet { position: relative; width: 849px; height: 1200px; background: var(--paper); color: var(--ink); }

  .brand { position: absolute; left: 47px; top: 57px; display: flex; align-items: center; gap: 10px; }
  .brand-dot { width: 25px; height: 25px; border-radius: 50%; background: var(--green); }
  .brand-name { font-family: 'Aleo', serif; font-weight: 400; font-size: 32px; letter-spacing: 1px; color: var(--ink); line-height: 1; margin-top: 8px; }

  .rating { position: absolute; left: 84px; top: 105px; display: flex; align-items: center; height: 20px; }
  .rating-word { font-family: 'Urbanist', sans-serif; font-weight: 800; font-size: 18px; letter-spacing: -0.5px; }
  .rating-bar { width: 103px; height: 20px; background: var(--green); margin-left: 13px; }
  .rating-source { margin-left: 14px; font-family: 'Urbanist', sans-serif; font-weight: 600; font-size: 14px; }

  .footer { position: absolute; left: 0; right: 0; top: 1042px; text-align: center; }
  .footer-rule { width: 205px; height: 2px; background: var(--green); margin: 0 auto; }
  .footer-site { font-family: 'Aleo', serif; font-weight: 700; font-size: 19px; margin-top: 8px; line-height: 22px; }
  .footer-address { font-family: 'Aleo', serif; font-weight: 400; font-size: 18.5px; color: var(--grey); line-height: 24px; }

  .phones { position: absolute; top: 1138px; left: 0; right: 0; }
  .phone { position: absolute; width: 170px; margin-left: -85px; text-align: center; }
  .phone-number { font-family: 'Urbanist', sans-serif; font-weight: 800; font-size: 18px; line-height: 22px; }
  .phone-label { font-family: 'Aleo', serif; font-weight: 700; font-size: 11.5px; color: var(--green); line-height: 16px; }
</style>
</head>
<body>
<div class="sheet">
  <header>
    <div class="brand">
      <span class="brand-dot"></span>
      <span class="brand-name">VELMORAN TRAVEL</span>
    </div>
    <div class="rating">
      <span class="rating-word">Excellent</span>
      <span class="rating-bar"></span>
      <span class="rating-source">Rate Harbor</span>
    </div>
  </header>

  <footer>
    <div class="footer">
      <div class="footer-rule"></div>
      <p class="footer-site">VelmoranTravel.com</p>
      <p class="footer-address">Harbour Lodge, Shannon Quay Road,<br>Ballyvarra, Co.Clare, Ireland.</p>
    </div>
    <div class="phones">
      <div class="phone" style="left:274px">
        <p class="phone-number">0800 041 7725</p>
        <p class="phone-label">UK Freefone</p>
      </div>
      <div class="phone" style="left:435px">
        <p class="phone-number">1855 304 6612</p>
        <p class="phone-label">USA &amp; Canada</p>
      </div>
      <div class="phone" style="left:595px">
        <p class="phone-number">+353 61 4820</p>
        <p class="phone-label">International</p>
      </div>
    </div>
  </footer>
</div>
</body>
</html>
```